Lumaform website scandinavian interior design

Existing website: http://lumaform-example.no/

Webdesign for interior designer Ragna Tvedtholm. The company name is Lumaform. Scandinavian interiør is known to be simple and elegant. The website will be in Norwegian, we are working on the text. The website needs to have a few more pages than just the front page. Here are the different titles of the pages:

1. Hjem
2. Om Lumaform
3. Tjenester og priser
4.. Kontakt oss

There should be Facebook and Instagram icons somewhere at the bottom of the website.

The logo we want to use is attached (pink with black print, see attachment )

We have attached images for inspiration. We want to use some of these colors. The color in the logo, The style should be elegant, modern and delicate.

It is imprtant that the website is user friendly.

Target Market(s)

People who want to decorate their home
Companies and public sector who need to redecorate

Industry/Entity Type

Interior Designer

Coding

Coded - Design and coding required

Number of Pages Required

5+ page

Font styles to use
Other font styles liked:
• see example in the logo breakdown

Requirements
Must have
• Elegant, modern and delicate design
Images of design, see examples attached
Colors similar to the pictures
Should not have
• Too bright colors
Pictures of people

```html
<!DOCTYPE html>
<html lang="no">
<head>
<meta charset="utf-8">
<title>Lumaform – scandinavian interior design</title>
<link rel="stylesheet" href="https://fonts.googleapis.com/css2?family=Lato:wght@300;400;700;900&family=Playfair+Display:ital@1&display=swap">
<style>
:root{
  --blush:#ecd3c9;
  --blush-soft:#f4e4dd;
  --blush-deep:#e2bfb2;
  --ink:#1f1f1f;
  --text:#4a4a4a;
  --muted:#8a8a8a;
  --white:#ffffff;
  --accent:#d6194b;
  --go:#3ecf8e;
  --line:#cfcfcf;
}
*{box-sizing:border-box;margin:0;padding:0}
html,body{width:1200px;height:3928px;overflow:hidden}
body{font-family:'Lato',sans-serif;color:var(--text);background:var(--white);position:relative}
.abs{position:absolute}
.photo{position:absolute;display:block}

/* header */
.site-header{position:absolute;left:0;top:0;width:1200px;height:80px;background:var(--blush)}
.header-tools{position:absolute;left:60px;top:26px;display:flex;gap:30px;align-items:center}
.tool{width:26px;height:26px;display:block}
.social-square{width:22px;height:22px;background:var(--ink);border-radius:4px;display:block}
.brand{position:absolute;left:520px;top:18px;width:160px;text-align:center;display:flex;align-items:center;justify-content:center;gap:10px}
.brand-dot{width:18px;height:18px;border-radius:50%;background:var(--blush-deep);border:1px solid var(--ink)}
.brand-name{font-family:'Lato',sans-serif;font-size:26px;font-weight:400;color:var(--ink)}
.brand-tag{position:absolute;top:50px;left:0;width:160px;text-align:center;font-size:9px;letter-spacing:2px;color:var(--ink);text-transform:uppercase}
.main-nav{position:absolute;right:50px;top:30px;display:flex;gap:34px;font-size:15px;color:var(--ink)}

/* hero */
.hero{position:absolute;left:0;top:80px;width:1200px;height:500px;background:linear-gradient(180deg,#8d8c8a 0%,#b9b5ae 45%,#6f6c69 100%)}
.hero-shade{position:absolute;inset:0;background:linear-gradient(90deg,rgba(30,30,30,.55) 0%,rgba(30,30,30,.15) 45%,rgba(30,30,30,.25) 100%)}
.hero-greeting{position:absolute;left:60px;top:105px;color:var(--white);font-size:48px;font-weight:700;letter-spacing:1px}
.hero-title{position:absolute;left:60px;top:160px;color:var(--white);font-size:76px;font-weight:700;line-height:1}
.hero-lede{position:absolute;left:62px;top:262px;color:var(--white);font-size:19px}
.btn{display:inline-block;background:var(--accent);color:var(--white);font-size:16px;padding:0 24px;height:44px;line-height:44px;border-radius:3px}
.hero .btn{position:absolute;left:60px;top:322px;font-size:20px;height:52px;line-height:52px;padding:0 30px}
.register{position:absolute;left:882px;top:68px;width:262px;height:360px;background:rgba(255,255,255,.18);border:1px solid rgba(255,255,255,.35);padding:22px 20px}
.register h2{font-size:18px;font-weight:400;color:var(--white);text-align:center;margin-bottom:14px}
.field{height:32px;background:var(--white);border-radius:2px;margin-bottom:12px;display:flex;align-items:center;gap:10px;padding:0 10px;font-size:13px;color:var(--muted)}
.field svg{width:14px;height:14px}
.register .btn-go{display:block;margin:24px auto 0;width:140px;height:34px;line-height:34px;text-align:center;background:var(--go);color:var(--white);font-size:15px;border-radius:3px}

/* section headings */
.heading{position:absolute;left:0;width:1200px;display:flex;align-items:center;justify-content:center;gap:22px;font-size:30px;font-weight:700;color:var(--ink)}
.heading::before,.heading::after{content:"";width:70px;height:2px;background:var(--ink)}

/* why */
.why-blob{left:88px;top:885px;width:200px;height:200px;border-radius:50%;background:var(--blush)}
.why-frame{left:168px;top:672px;width:390px;height:400px;border:2px solid var(--ink)}
.why-photo{left:178px;top:684px;width:374px;height:372px;background:linear-gradient(160deg,#6c6a66,#a4907a 55%,#3a3836)}
.why-heading{left:596px;top:688px;display:flex;align-items:center;gap:16px;font-size:30px;font-weight:700;color:var(--ink)}
.why-heading::before{content:"";width:60px;height:2px;background:var(--ink)}
.why-copy{left:612px;top:740px;width:400px;font-size:13px;line-height:1.6;color:var(--text)}
.why-points{left:612px;top:860px;display:flex;gap:24px}
.point{width:170px;height:170px;border-radius:50%;background:var(--blush-soft);text-align:center;padding-top:26px}
.point svg{width:34px;height:34px}
.point h3{font-size:13px;font-weight:700;color:var(--ink);margin:8px 0 4px}
.point p{font-size:10px;line-height:1.4;padding:0 22px;color:var(--text)}
.point small{display:block;font-size:9px;margin-top:6px;color:var(--ink)}

/* services */
.services-band{left:0;top:1360px;width:1200px;height:260px;background:var(--blush)}
.services-grid{left:192px;top:1226px;display:flex;gap:20px}
.service-card{width:260px;height:328px;background:var(--white);box-shadow:0 2px 10px rgba(0,0,0,.12);position:relative;overflow:hidden}
.service-card .photo{left:0;top:0;width:260px;height:170px}
.service-card h3{position:absolute;left:22px;top:194px;font-size:17px;font-weight:700;color:var(--ink)}
.service-card p{position:absolute;left:22px;top:226px;width:210px;font-size:11px;line-height:1.5}
.service-card .more{position:absolute;left:22px;top:280px;font-size:10px;color:var(--ink)}
.service-card .notch{position:absolute;left:180px;top:262px;width:100px;height:100px;border-radius:50%;background:var(--blush-soft)}
.services-cta{left:530px;top:1610px;width:140px;text-align:center;padding:0}

/* works */
.works-cta{left:530px;top:2700px;width:140px;text-align:center;padding:0}

/* reviews */
.reviews-band{left:0;top:2820px;width:1200px;height:400px;background:var(--blush)}
.review-card{top:2940px;width:352px;height:150px;background:var(--white);text-align:center;padding-top:26px;box-shadow:0 2px 8px rgba(0,0,0,.08)}
.review-card h3{font-size:14px;font-weight:700;color:var(--ink)}
.review-card .role{font-size:10px;color:var(--muted);margin:4px 0 14px}
.review-card p{font-size:11px;line-height:1.5;padding:0 70px}
.review-card .quote{font-family:'Playfair Display',serif;color:var(--accent);font-size:34px;line-height:1;margin-top:6px}
.dots{left:570px;top:3122px;display:flex;gap:8px}
.dots span{width:8px;height:8px;border-radius:50%;background:var(--muted)}
.dots span.on{background:var(--ink)}

/* blog */
.blog-card{top:3320px;width:410px;height:280px;position:absolute}
.blog-frame{position:absolute;left:80px;top:0;width:330px;height:280px;border:2px solid var(--ink);border-radius:22px}
.blog-circle{position:absolute;left:118px;top:-30px;width:56px;height:56px;border-radius:50%;background:var(--blush)}
.blog-card .photo{left:0;top:40px;width:170px;height:200px}
.blog-card h3{position:absolute;left:190px;top:58px;width:200px;font-size:18px;font-weight:700;color:var(--ink);line-height:1.25}
.blog-card .date{position:absolute;left:190px;top:108px;font-size:10px;color:var(--muted)}
.blog-card p{position:absolute;left:190px;top:130px;width:200px;font-size:11px;line-height:1.5}

/* footer */
.site-footer{left:0;top:3680px;width:1200px;height:248px;background:var(--blush)}
.footer-about{left:140px;top:110px;width:240px;font-size:11px;line-height:1.55;color:var(--ink)}
.footer-contact{left:440px;top:110px;font-size:11px;line-height:1.7;color:var(--ink)}
.footer-mail{left:640px;top:110px;font-size:11px;line-height:1.7;color:var(--ink)}
.footer-copy{left:860px;top:124px;font-size:11px;color:var(--ink)}
.footer-social{left:560px;top:196px;display:flex;gap:40px}
</style>
</head>
<body>

<header class="site-header">
  <div class="header-tools">
    <svg class="tool" viewBox="0 0 26 26" aria-label="Meny"><rect x="3" y="6" width="20" height="2.5" fill="#1f1f1f"/><rect x="3" y="12" width="20" height="2.5" fill="#1f1f1f"/><rect x="3" y="18" width="20" height="2.5" fill="#1f1f1f"/></svg>
    <svg class="tool" viewBox="0 0 26 26" aria-label="Søk"><circle cx="11" cy="11" r="7" fill="none" stroke="#1f1f1f" stroke-width="2.5"/><line x1="16" y1="16" x2="23" y2="23" stroke="#1f1f1f" stroke-width="2.5"/></svg>
    <span class="social-square" aria-label="Sosiale medier"></span>
    <span class="social-square" aria-label="Sosiale medier"></span>
  </div>
  <div class="brand">
    <span class="brand-dot"></span><span class="brand-name">Lumaform</span>
    <span class="brand-tag">interiørdesign</span>
  </div>
  <nav class="main-nav">
    <span>Hjem</span><span>Om Lumaform</span><span>Tjenester og priser</span><span>Kontakt oss</span>
  </nav>
</header>

<section class="hero">
  <div class="photo" role="img" aria-label="Lys stue med grå sofa, runde bord og mønstret teppe" style="inset:0;background:linear-gradient(180deg,#9a9690 0%,#c7c1b8 45%,#8a847d 100%)"></div>
  <div class="hero-shade"></div>
  <div class="hero-greeting">Welcome To</div>
  <h1 class="hero-title">Lumaform</h1>
  <p class="hero-lede">Lets design your dream house together.</p>
  <span class="btn">Get Started</span>
  <form class="register">
    <h2>Register account</h2>
    <div class="field"><svg viewBox="0 0 14 14"><circle cx="7" cy="4.5" r="3" fill="#8a8a8a"/><path d="M1 14c0-4 12-4 12 0z" fill="#8a8a8a"/></svg>Your Name</div>
    <div class="field"><svg viewBox="0 0 14 14"><circle cx="7" cy="4.5" r="3" fill="#8a8a8a"/><path d="M1 14c0-4 12-4 12 0z" fill="#8a8a8a"/></svg>Username</div>
    <div class="field"><svg viewBox="0 0 14 14"><rect x="1" y="3" width="12" height="8" fill="none" stroke="#8a8a8a"/><path d="M1 3l6 5 6-5" fill="none" stroke="#8a8a8a"/></svg>Your Email</div>
    <div class="field"><svg viewBox="0 0 14 14"><rect x="2" y="6" width="10" height="7" fill="#8a8a8a"/><path d="M4 6V4a3 3 0 016 0v2" fill="none" stroke="#8a8a8a"/></svg>Password</div>
    <div class="field"><svg viewBox="0 0 14 14"><rect x="2" y="6" width="10" height="7" fill="#8a8a8a"/><path d="M4 6V4a3 3 0 016 0v2" fill="none" stroke="#8a8a8a"/></svg>Confirm Password</div>
    <span class="btn-go">Register</span>
  </form>
</section>

<section class="why">
  <div class="abs why-blob"></div>
  <div class="abs why-frame"></div>
  <div class="photo why-photo" role="img" aria-label="Sideboard i eik med lampe, speil og dekor mot mørk vegg"></div>
  <h2 class="abs why-heading">Why Lumaform</h2>
  <p class="abs why-copy">Vi skaper rolige og lyse rom med skandinavisk enkelhet. Hvert prosjekt starter med en samtale om hvordan du lever, og ender i et hjem som føles naturlig, varmt og gjennomtenkt i hver detalj.</p>
  <div class="abs why-points">
    <div class="point">
      <svg viewBox="0 0 34 34"><circle cx="17" cy="11" r="6" fill="none" stroke="#1f1f1f" stroke-width="2"/><path d="M5 31c0-8 24-8 24 0" fill="none" stroke="#1f1f1f" stroke-width="2"/></svg>
      <h3>Design Experts</h3>
      <p>Erfarne designere med øye for lys, form og materialer.</p>
      <small>Les mer</small>
    </div>
    <div class="point">
      <svg viewBox="0 0 34 34"><path d="M17 29S4 21 4 12a6.5 6.5 0 0113-2 6.5 6.5 0 0113 2c0 9-13 17-13 17z" fill="none" stroke="#1f1f1f" stroke-width="2"/></svg>
      <h3>Happy Customers</h3>
      <p>Fornøyde kunder i private hjem og offentlige bygg.</p>
      <small>Les mer</small>
    </div>
    <div class="point">
      <svg viewBox="0 0 34 34"><path d="M5 11l12-6 12 6v13l-12 6-12-6z M5 11l12 6 12-6 M17 17v13" fill="none" stroke="#1f1f1f" stroke-width="2"/></svg>
      <h3>Product &amp; Services</h3>
      <p>Utvalgte møbler og tjenester fra idé til ferdig rom.</p>
      <small>Les mer</small>
    </div>
  </div>
</section>

<section class="services">
  <h2 class="heading" style="top:1160px">Services</h2>
  <div class="abs services-band"></div>
  <div class="abs services-grid">
    <article class="service-card">
      <div class="photo" role="img" aria-label="Spisestue med mørkt bord og stoler" style="background:linear-gradient(160deg,#3b2a28,#8b6d5c)"></div>
      <h3>Customised Designs</h3>
      <p>Løsninger skreddersydd for ditt rom, din stil og ditt budsjett.</p>
      <span class="more">Read More</span>
      <span class="notch"></span>
    </article>
    <article class="service-card">
      <div class="photo" role="img" aria-label="Soverom med gul sengeteppe og lamper" style="background:linear-gradient(160deg,#4a3a30,#c9a25a 60%,#e9e1d6)"></div>
      <h3>Hassle-free Execution</h3>
      <p>Vi styrer hele prosjektet slik at du kan lene deg tilbake.</p>
      <span class="more">Read More</span>
      <span class="notch"></span>
    </article>
    <article class="service-card">
      <div class="photo" role="img" aria-label="Visualisering av stue med grå lenestoler" style="background:linear-gradient(160deg,#5a5552,#b6aea6 60%,#ded8d2)"></div>
      <h3>3D Design view</h3>
      <p>Se rommet ditt i 3D før et eneste møbel er kjøpt.</p>
      <span class="more">Read More</span>
      <span class="notch"></span>
    </article>
  </div>
  <span class="abs btn services-cta">More Services</span>
</section>

<section class="works">
  <h2 class="heading" style="top:1786px">Our Recent Works</h2>
  <div class="photo" role="img" aria-label="Lys stue med trapp og peis" style="left:152px;top:1840px;width:282px;height:390px;background:linear-gradient(160deg,#e4e0da,#9f988f)"></div>
  <div class="photo" role="img" aria-label="Moderne hus med basseng og glassvegger" style="left:452px;top:1840px;width:282px;height:390px;background:linear-gradient(160deg,#d9dde0,#6d7c7a 60%,#3e5a5e)"></div>
  <div class="photo" role="img" aria-label="Lys stue med trapp og rosa sofa" style="left:752px;top:1840px;width:302px;height:390px;background:linear-gradient(160deg,#efe9e4,#c8b7ad)"></div>
  <div class="photo" role="img" aria-label="Hvit lenestol med gulvlampe og hylle" style="left:152px;top:2250px;width:282px;height:390px;background:linear-gradient(160deg,#efece8,#bdb6ad)"></div>
  <div class="photo" role="img" aria-label="Stort kjøkken med øy og barkrakker" style="left:452px;top:2250px;width:602px;height:390px;background:linear-gradient(160deg,#dcd8d3,#8c8178 55%,#4c4642)"></div>
  <span class="abs btn works-cta">More Portfolio</span>
</section>

<section class="reviews">
  <div class="abs reviews-band"></div>
  <h2 class="heading" style="top:2870px">Client Reviews</h2>
  <article class="abs review-card" style="left:190px">
    <h3>Maren Holt</h3>
    <div class="role">Privatkunde</div>
    <p>Et varmt og lyst hjem, akkurat slik vi drømte om det.</p>
    <div class="quote">“</div>
  </article>
  <article class="abs review-card" style="left:662px">
    <h3>Sigrid Lunde</h3>
    <div class="role">Kontorsjef</div>
    <p>Profesjonelt, ryddig og et resultat hele teamet elsker.</p>
    <div class="quote">“</div>
  </article>
  <div class="abs dots"><span></span><span class="on"></span><span></span></div>
</section>

<section class="blog">
  <h2 class="heading" style="top:3252px">Latest Blog</h2>
  <article class="blog-card" style="left:190px">
    <div class="blog-frame"></div>
    <div class="blog-circle"></div>
    <div class="photo" role="img" aria-label="Sofa med puter foran gul vegg" style="background:linear-gradient(160deg,#e2b84a,#d9cfc2 60%,#8a7f74)"></div>
    <h3>Post Tittel Her</h3>
    <span class="date">12. mars</span>
    <p>Små grep som gir stuen mer lys, ro og varme gjennom hele vinteren.</p>
  </article>
  <article class="blog-card" style="left:620px">
    <div class="blog-frame"></div>
    <div class="blog-circle"></div>
    <div class="photo" role="img" aria-label="Soverom i grå og hvite toner" style="background:linear-gradient(160deg,#7a7b7e,#c6c2bc 60%,#e8e4de)"></div>
    <h3>Post Tittel Her</h3>
    <span class="date">4. april</span>
    <p>Slik velger du tekstiler og farger som skaper et rolig soverom.</p>
  </article>
</section>

<footer class="abs site-footer">
  <div class="brand" style="left:520px;top:32px">
    <span class="brand-dot"></span><span class="brand-name">Lumaform</span>
    <span class="brand-tag">interiørdesign</span>
  </div>
  <p class="abs footer-about">Lumaform skaper enkle og elegante rom for hjem, bedrifter og offentlig sektor i hele Norge.</p>
  <p class="abs footer-contact">Postboks 100<br>0150 Oslo</p>
  <p class="abs footer-mail">post@lumaform-example.no<br>+47 000 00 000</p>
  <p class="abs footer-copy">Copyright © 2024 Lumaform</p>
  <div class="abs footer-social">
    <span class="social-square" aria-label="Sosiale medier"></span>
    <span class="social-square" aria-label="Sosiale medier"></span>
  </div>
</footer>

</body>
</html>
```